New custom software business needs a Wordpress site

We need a Wordpress site for a new company based out of Chicago called 'Vellora Consulting'. Using a mix of on and off-shore resources we build custom software solutions, mainly focusing on small to medium sized companies. We help our customers "aspire" to do great things.
We have a basic site up here: https://brindlewave.example/. We worked on the content for it but not the branding. For now, this houses all the pages (except for a Contact Us page we'll be adding soon) for the foreseeable future.
We also have a new logo (attached) that we'd like to base the styling/colors on.
Target Market(s)
Small to medium sized companies that require tech resources
Industry/Entity Type
Software
Nice to have
- Teamwork, tech, professional but not elitist

```html
<!DOCTYPE html>
<html lang="en">
<head>
<meta charset="utf-8">
<title>Vellora Consulting — Custom Software Development</title>
<link href="https://fonts.googleapis.com/css2?family=Audiowide&family=Exo+2:wght@500;600&family=Poppins:wght@400;500;600&display=swap" rel="stylesheet">
<style>
:root{
  --blue:#0b4ea2;
  --blue-dark:#083f86;
  --blue-light:#2f78d1;
  --ink:#1c1c1c;
  --text:#3a3a3a;
  --muted:#8a8f99;
  --pale:#e6eef8;
  --line:#d7dbe2;
  --white:#fff;
  --footer-bottom:#2a2f3d;
}
*{box-sizing:border-box;margin:0;padding:0}
html,body{width:1200px;height:4428px;overflow:hidden}
body{font-family:"Poppins",sans-serif;color:var(--text);background:var(--white);position:relative}
.wrap{position:absolute;left:160px;width:880px}
h2.section-title{font-family:"Audiowide",sans-serif;font-weight:400;font-size:29px;color:var(--ink);text-align:center;letter-spacing:1px;text-transform:uppercase}
h2.section-title span{color:var(--blue)}
.title-rule{width:50px;height:3px;background:var(--blue);margin:14px auto 0}
a{text-decoration:none;color:inherit}

/* top bar */
.topbar{position:absolute;top:0;left:0;width:1200px;height:43px;border-bottom:1px solid var(--line)}
.topbar .contact{position:absolute;left:160px;top:8px;display:flex;gap:20px;font-size:14px;color:var(--ink)}
.topbar .contact span{display:flex;align-items:center;gap:8px}
.icon-dot{width:26px;height:26px;border-radius:50%;background:var(--blue);display:inline-flex;align-items:center;justify-content:center}
.talk{position:absolute;right:162px;top:4px;width:130px;height:34px;background:var(--blue);color:#fff;font-size:13px;display:flex;align-items:center;justify-content:center}

/* nav */
.nav{position:absolute;top:43px;left:0;width:1200px;height:89px}
.brand{position:absolute;left:160px;top:17px;display:flex;align-items:center;gap:10px}
.brand-mark{width:22px;height:22px;background:var(--blue)}
.brand-name{font-family:"Exo 2",sans-serif;font-weight:600;font-size:26px;color:var(--blue);letter-spacing:1px;line-height:1}
.brand-sub{font-family:"Exo 2",sans-serif;font-size:10px;color:var(--blue-light);letter-spacing:3px}
.menu{position:absolute;right:162px;top:36px;display:flex;gap:32px;font-size:13px;font-weight:500;color:var(--ink);text-transform:uppercase}

/* hero */
.hero{position:absolute;top:132px;left:0;width:1200px;height:564px;background:linear-gradient(90deg,#0b4ea2 0%,#2b5f9f 30%,#9eaec4 55%,#d7d9dc 80%,#c4c7cb 100%)}
.hero-copy{position:absolute;left:160px;top:198px}
.hero h1{font-family:"Audiowide",sans-serif;font-weight:400;font-size:34px;line-height:45px;color:#fff}
.hero .btn-contact{display:inline-block;margin-top:20px;background:#fff;color:var(--ink);font-size:14px;font-weight:500;padding:8px 14px}

/* services */
.services{position:absolute;top:696px;left:0;width:1200px;height:1018px;overflow:hidden}
.deco-circle{position:absolute;border-radius:50%;background:var(--pale)}
.services h2{position:absolute;top:88px;width:1200px}
.services .title-rule{position:absolute;top:140px;left:575px;margin:0}
.service-art{position:absolute;border-radius:4px;background:linear-gradient(135deg,#eaf1fb,#b9d1ef 60%,#2a63b5)}
.service-text{position:absolute;width:440px}
.service-text .num{font-family:"Audiowide",sans-serif;font-size:42px;color:var(--ink);line-height:1}
.service-text h3{font-family:"Exo 2",sans-serif;font-weight:600;font-size:28px;color:var(--blue);margin:12px 0 14px}
.service-text p{font-size:13.5px;line-height:22px}
.know{display:inline-block;margin-top:18px;font-size:14px;font-weight:600;color:var(--blue);border-bottom:2px solid var(--blue)}

/* about */
.about{position:absolute;top:1714px;left:0;width:1200px;height:524px;background:var(--pale)}
.about h2{position:absolute;top:90px;width:1200px}
.about .title-rule{position:absolute;top:140px;left:575px;margin:0}
.about-copy{position:absolute;left:160px;top:152px;width:880px;text-align:center;font-size:13.5px;line-height:22px}
.about-copy p{margin-bottom:10px}
.btn{display:inline-block;background:var(--blue);color:#fff;font-family:"Exo 2",sans-serif;font-weight:600;font-size:14px}
.about .btn{position:absolute;left:545px;top:395px;width:110px;height:36px;line-height:36px;text-align:center}

/* testimonials */
.testimonials{position:absolute;top:2238px;left:0;width:1200px;height:535px}
.testimonials h2{position:absolute;top:88px;width:1200px}
.testimonials .title-rule{position:absolute;top:140px;left:575px;margin:0}
.quote-card{position:absolute;top:200px;width:420px;height:230px;background:#fff;box-shadow:0 2px 10px rgba(0,0,0,.12);text-align:center}
.quote-mark{font-family:"Audiowide",sans-serif;font-size:80px;color:var(--blue);line-height:1;height:56px;margin-top:10px}
.stars{color:#f2a900;font-size:13px;letter-spacing:5px}
.review-dot{position:absolute;right:18px;top:16px;width:24px;height:24px;border-radius:50%;border:3px solid #c9ced6}
.quote-card p{font-size:13.5px;line-height:24px;padding:12px 32px 0}
.quote-card .who{font-weight:600;font-size:15px;color:var(--ink);margin-top:10px}
.arrow-btn{position:absolute;width:45px;height:45px;display:flex;align-items:center;justify-content:center}
.arrow-prev{left:81px;top:323px;border:1px solid var(--ink)}
.arrow-next{left:1069px;top:294px;background:var(--blue)}

/* clients */
.clients{position:absolute;top:2773px;left:0;width:1200px;height:369px;background:var(--pale)}
.clients h2{position:absolute;top:90px;width:1200px}
.clients .title-rule{position:absolute;top:140px;left:575px;margin:0}
.client-row{position:absolute;left:158px;top:175px;display:flex;gap:17px}
.client-box{width:162px;height:100px;background:#fff;display:flex;align-items:center;justify-content:center;gap:8px;font-family:"Poppins",sans-serif;font-weight:500;font-size:19px;color:var(--ink)}
.client-box i{width:14px;height:14px;border-radius:50%;background:var(--blue);display:block}

/* inquiry */
.inquiry{position:absolute;top:3142px;left:0;width:1200px;height:924px}
.inquiry h2{position:absolute;top:90px;width:1200px}
.inquiry .title-rule{position:absolute;top:140px;left:575px;margin:0}
.field{position:absolute;height:40px;border:1px solid var(--line);font-size:12.5px;color:#555;padding:10px 12px}
.field.msg{height:103px}
.inquiry .btn{position:absolute;left:556px;top:499px;width:88px;height:38px;line-height:38px;text-align:center}
.office-art{position:absolute;left:0;top:622px;width:1200px;height:302px;background:linear-gradient(180deg,#ffffff 0%,#eef3fa 45%,#d9e4f3 100%)}

/* footer */
.footer{position:absolute;top:4066px;left:0;width:1200px;height:309px;background:var(--blue)}
.foot-brand{position:absolute;left:160px;top:110px;text-align:center;width:210px}
.foot-brand .mark{width:40px;height:40px;background:#fff;margin:0 auto 18px}
.foot-brand .name{font-family:"Exo 2",sans-serif;font-weight:600;font-size:36px;color:#fff;letter-spacing:2px;line-height:1}
.foot-brand .sub{font-family:"Exo 2",sans-serif;font-size:13px;color:#fff;letter-spacing:4px;margin-top:4px}
.footer h4{font-family:"Exo 2",sans-serif;font-weight:600;font-size:17px;color:#fff;text-transform:uppercase}
.quick{position:absolute;left:528px;top:70px}
.quick ul{list-style:none;margin-top:18px}
.quick li{color:#fff;font-size:13px;margin-bottom:17px}
.quick li::before{content:"›";margin-right:12px}
.contacts{position:absolute;left:813px;top:70px;width:240px}
.c-item{display:flex;gap:14px;margin-top:18px;color:#fff;font-size:13px;line-height:21px}
.c-ico{flex:none;width:36px;height:36px;border:2px solid #fff;border-radius:50%;display:flex;align-items:center;justify-content:center}
.c-item b{font-weight:600;font-size:12px}
.copyright{position:absolute;top:4375px;left:0;width:1200px;height:53px;background:var(--footer-bottom);color:#fff;font-size:13px;text-align:center;line-height:53px}
</style>
</head>
<body>

<header class="topbar">
  <div class="contact">
    <span><i class="icon-dot"><svg width="12" height="12" viewBox="0 0 24 24"><path fill="#fff" d="M6.6 10.8a15.1 15.1 0 0 0 6.6 6.6l2.2-2.2c.3-.3.7-.4 1-.2 1.1.4 2.3.6 3.6.6.6 0 1 .4 1 1V20c0 .6-.4 1-1 1A17 17 0 0 1 3 4c0-.6.4-1 1-1h3.5c.6 0 1 .4 1 1 0 1.3.2 2.5.6 3.6.1.3 0 .7-.2 1z"/></svg></i>123 456 7890</span>
    <span><i class="icon-dot"><svg width="12" height="12" viewBox="0 0 24 24"><path fill="#fff" d="M3 6h18v12H3z M3 6l9 7 9-7" stroke="#0b4ea2" stroke-width="1.5"/></svg></i>info@vellora.example</span>
  </div>
  <a class="talk" href="#">Lets' Talk</a>
</header>

<nav class="nav">
  <div class="brand">
    <div class="brand-mark"></div>
    <div><div class="brand-name">VELLORA</div><div class="brand-sub">CONSULTING</div></div>
  </div>
  <div class="menu"><a href="#">Services</a><a href="#">Why Vellora?</a><a href="#">Vellora Leadership</a><a href="#">Contact Us</a></div>
</nav>

<section class="hero" role="img" aria-label="Photo of two colleagues reviewing printed documents together in a bright office">
  <div class="hero-copy">
    <h1>We Specialize In<br>Custom Software<br>Development</h1>
    <a class="btn-contact" href="#">Contact Us</a>
  </div>
</section>

<section class="services">
  <div class="deco-circle" style="left:-90px;top:20px;width:250px;height:330px"></div>
  <div class="deco-circle" style="left:1040px;top:400px;width:300px;height:330px"></div>
  <h2 class="section-title"><span>Our</span> Services</h2>
  <div class="title-rule"></div>

  <div class="service-art" style="left:160px;top:198px;width:385px;height:310px" role="img" aria-label="Illustration of a team working with dashboards and charts"></div>
  <div class="service-text" style="left:605px;top:280px">
    <div class="num">01.</div>
    <h3>Custom Solution Delivery</h3>
    <p>Vellora offers a range of services focused on helping businesses and organizations deliver software solutions to their customers or users.</p>
    <a class="know" href="#">Know More →</a>
  </div>

  <div class="service-text" style="left:160px;top:686px">
    <div class="num">02.</div>
    <h3>Staff Augmentation</h3>
    <p>Let Vellora help you supplement your existing software development teams with additional resources and expertise. We provided access to experienced</p>
    <a class="know" href="#">Know More →</a>
  </div>
  <div class="service-art" style="left:620px;top:628px;width:422px;height:290px" role="img" aria-label="Illustration of developers collaborating around a circular workflow with a forward arrow"></div>
</section>

<section class="about">
  <h2 class="section-title"><span>About</span> Vellora Consulting</h2>
  <div class="title-rule"></div>
  <div class="about-copy">
    <p>Welcome to Vellora, a software consulting company specializing in serving small to medium size businesses.We understand the unique challenges and opportunities that these companies face, and we are dedicated to helping them succeed through innovative technology solutions.</p>
    <p>Our team of experienced professionals has a diverse range of skills &amp; expertise, making us well-equipped to handle any project, big or small. We specialize in custom software development, working closely with our clients to understand their specific needs &amp; build solutions that meet their requirements.</p>
    <p>From developing web &amp; mobile applications to implementing cloud-based systems and integrating with existing platforms, we have the tools &amp; knowledge to deliver results that drive success.</p>
  </div>
  <a class="btn" href="#">Learn More</a>
</section>

<section class="testimonials">
  <h2 class="section-title"><span>What</span> Our Clients Say</h2>
  <div class="title-rule"></div>
  <div class="arrow-btn arrow-prev"><svg width="10" height="10" viewBox="0 0 10 10"><path d="M6.5 1.5L3 5l3.5 3.5" fill="none" stroke="#1c1c1c" stroke-width="1.5"/></svg></div>
  <article class="quote-card" style="left:160px">
    <span class="review-dot"></span>
    <div class="quote-mark">“</div>
    <div class="stars">★★★★★</div>
    <p>Lorem Ipsum is simply dummy text of the printing and typesetting industry. Lorem Ipsum has been the industry's standard dummy text ever since the 1500s, when an unknown printer took a galley</p>
    <div class="who">John Doe</div>
  </article>
  <article class="quote-card" style="left:617px">
    <span class="review-dot"></span>
    <div class="quote-mark">“</div>
    <div class="stars">★★★★★</div>
    <p>Lorem Ipsum is simply dummy text of the printing and typesetting industry. Lorem Ipsum has been the industry's standard dummy text ever since the 1500s, when an unknown printer took a galley</p>
    <div class="who">Marlo Quinn</div>
  </article>
  <div class="arrow-btn arrow-next"><svg width="10" height="10" viewBox="0 0 10 10"><path d="M3.5 1.5L7 5 3.5 8.5" fill="none" stroke="#fff" stroke-width="1.5"/></svg></div>
</section>

<section class="clients">
  <h2 class="section-title"><span>Our</span> Clients</h2>
  <div class="title-rule"></div>
  <div class="client-row">
    <div class="client-box"><i></i>Norvex</div>
    <div class="client-box"><i></i>Quillstack</div>
    <div class="client-box"><i></i>Orbitly</div>
    <div class="client-box"><i></i>Tessaly</div>
    <div class="client-box"><i></i>Lumacraft</div>
  </div>
</section>

<section class="inquiry">
  <h2 class="section-title"><span>Quick</span> Inquiry</h2>
  <div class="title-rule"></div>
  <div class="field" style="left:160px;top:224px;width:418px">Frist Name*</div>
  <div class="field" style="left:621px;top:224px;width:419px">Last Name*</div>
  <div class="field" style="left:160px;top:286px;width:418px">Phone*</div>
  <div class="field" style="left:621px;top:286px;width:419px">Email*</div>
  <div class="field msg" style="left:160px;top:348px;width:880px">Message*</div>
  <a class="btn" href="#">Submit</a>
  <div class="office-art" role="img" aria-label="Illustration of people working at desks in a modern office with plants and shelving"></div>
</section>

<footer class="footer">
  <div class="foot-brand">
    <div class="mark"></div>
    <div class="name">VELLORA</div>
    <div class="sub">CONSULTING</div>
  </div>
  <div class="quick">
    <h4>Quick Links</h4>
    <ul><li>Home</li><li>About Us</li><li>Wholesale</li><li>Services</li><li>Contact Us</li></ul>
  </div>
  <div class="contacts">
    <h4>Contact Details</h4>
    <div class="c-item"><span class="c-ico"><svg width="14" height="16" viewBox="0 0 14 18"><path d="M7 1a6 6 0 0 0-6 6c0 4.5 6 10 6 10s6-5.5 6-10a6 6 0 0 0-6-6z" fill="none" stroke="#fff" stroke-width="1.6"/><circle cx="7" cy="7" r="2" fill="#fff"/></svg></span><span>Street Name, City Name,<br>State Zipcode</span></div>
    <div class="c-item"><span class="c-ico"><svg width="14" height="14" viewBox="0 0 24 24"><path fill="#fff" d="M6.6 10.8a15.1 15.1 0 0 0 6.6 6.6l2.2-2.2c.3-.3.7-.4 1-.2 1.1.4 2.3.6 3.6.6.6 0 1 .4 1 1V20c0 .6-.4 1-1 1A17 17 0 0 1 3 4c0-.6.4-1 1-1h3.5c.6 0 1 .4 1 1 0 1.3.2 2.5.6 3.6.1.3 0 .7-.2 1z"/></svg></span><span><b>PHONE</b><br>+ 1 123 456 7890</span></div>
    <div class="c-item"><span class="c-ico"><svg width="14" height="12" viewBox="0 0 20 14"><rect x="1" y="1" width="18" height="12" fill="none" stroke="#fff" stroke-width="1.6"/><path d="M1 1l9 7 9-7" fill="none" stroke="#fff" stroke-width="1.6"/></svg></span><span><b>EMAIL</b><br>info@vellora.example</span></div>
  </div>
</footer>
<div class="copyright">© 2023 Vellora Consulting. All Rights Reserved.</div>

</body>
</html>
```